A New and modern Business Card for Tarvish Commerce Partners Ltd

New and modern Logo and Business Card Attached is the current logo/business card designCurrently the business is called "Tarvish & Co." or TCP Ltd for short. This is subject to change.This business specialises in Telecoms and Energy. We work with the major networks (QX, Z7, etc) and also offer Energy Products saving clients money off their energy bills.These are business to business services.The current design incorporates a Pheonix, indicating rebirth, starting something new.We would like to maintain the Phoenix element but a newer modern style.We love colours in the logo 3 max.The aim of this is to be ultra slick and modern. I envisage Tarvish & Co. on one side of the card with long descriptions on the other side.Side 1:TCP Ltd/Logo?Side 2:TCP Ltd/Logo/Graphic?Brogan & Co.Name:Address:Phone:Email:The design is mostly flexible but must incorporate a Phoenix.For example "Tarvish & Co." with a block phoenix behind the text...up to you.

Industry/Entity Type

Telecommunications

Contact Information for Business Card

Tarvish & Co.
Address:
Name:
Phone:
Email:

Logo Text

Tarvish & Co.

Colors
33a6d7
0792cd
acd037
9bcb3c
f78f20
fece3e

Requirements
Must have
• Phoenix
• 3/4 colours max
• Blue representing Technology (wireless)
• Green for Eco Energy
• Orange for Phoenix
• White business card background
Should not have
• phoenix must not all be red/ orange fire, we are a technology service company and the phoenix colours must represent this. Fire is not representative of our company.

```html
<!DOCTYPE html>
<html lang="en">
<head>
<meta charset="utf-8">
<title>Tarvish Commerce Partners Ltd – Business Card</title>
<link rel="stylesheet" href="https://fonts.googleapis.com/css2?family=Montserrat:wght@600&family=Roboto:wght@400;500&display=swap">
<style>
  :root {
    --stage: #2b2d31;
    --card-white: #ffffff;
    --card-edge: #dfe3ea;
    --card-edge-dark: #c9cfd9;
    --brand-blue: #3b5fa9;
    --text-blue-soft: #51669a;
    --accent-green: #a9d13a;
  }
  * { box-sizing: border-box; margin: 0; padding: 0; }
  html, body {
    width: 1200px;
    height: 900px;
    overflow: hidden;
    background: var(--stage);
  }
  .stage {
    position: relative;
    width: 1200px;
    height: 900px;
    display: flex;
    align-items: center;
    justify-content: center;
    gap: 60px;
  }
  .card {
    position: relative;
    width: 525px;
    height: 300px;
    border-radius: 28px;
    background: var(--card-white);
    box-shadow: 0 4px 0 var(--card-edge-dark), 0 8px 0 var(--card-edge), 0 12px 0 var(--card-edge-dark), 0 24px 40px rgba(0,0,0,0.45);
    overflow: hidden;
  }

  /* Front side */
  .card-front .brand {
    position: absolute;
    left: 50%;
    top: 50%;
    transform: translate(-50%, -50%);
    display: flex;
    align-items: center;
    gap: 18px;
    font-family: "Montserrat", sans-serif;
    font-weight: 600;
    color: var(--brand-blue);
    white-space: nowrap;
  }
  .brand-dot {
    width: 46px;
    height: 46px;
    border-radius: 50%;
    background: var(--accent-green);
    flex: none;
  }
  .brand-name {
    display: flex;
    flex-direction: column;
    line-height: 1;
  }
  .brand-main {
    font-size: 50px;
    letter-spacing: 8px;
  }
  .brand-sub {
    margin-top: 8px;
    font-size: 13px;
    letter-spacing: 2.4px;
  }

  /* Back side */
  .contact {
    position: absolute;
    left: 64px;
    top: 48px;
    font-family: "Roboto", sans-serif;
    font-weight: 400;
    color: var(--text-blue-soft);
  }
  .contact-name {
    font-weight: 500;
    font-size: 20px;
    color: var(--brand-blue);
    margin-bottom: 18px;
  }
  .contact-line {
    font-size: 11.5px;
    letter-spacing: 1px;
    line-height: 1.65;
    white-space: nowrap;
  }
  .contact-gap { margin-top: 10px; }
  .back-brand {
    position: absolute;
    right: 48px;
    bottom: 52px;
    display: flex;
    align-items: center;
    gap: 14px;
    font-family: "Montserrat", sans-serif;
    font-weight: 600;
    font-size: 26px;
    letter-spacing: 2px;
    color: var(--brand-blue);
    white-space: nowrap;
  }
  .back-brand .brand-dot {
    width: 40px;
    height: 40px;
  }
</style>
</head>
<body>
  <main class="stage">
    <section class="card card-front" aria-label="Card front">
      <div class="brand">
        <span class="brand-dot" aria-hidden="true"></span>
        <span class="brand-name">
          <span class="brand-main">TARVISH</span>
          <span class="brand-sub">Commerce Partners Limited</span>
        </span>
      </div>
    </section>

    <section class="card card-back" aria-label="Card back">
      <div class="contact">
        <p class="contact-name">John doe</p>
        <p class="contact-line">+88 888 8888</p>
        <p class="contact-line contact-gap">name@example.com</p>
        <p class="contact-line">Address and Location</p>
        <p class="contact-line">street number 00000</p>
      </div>
      <div class="back-brand">
        <span class="brand-dot" aria-hidden="true"></span>
        <span>TCP Ltd</span>
      </div>
    </section>
  </main>
</body>
</html>
```